Aviation security consulting company needs a website

We need a website design for Brisk Holloway, and aviation security consulting company. Brisk Holloway (www.briskholloway.example) is an aviation security consulting company that works with government and industry stakeholders in over 60 countries on aviation security strategy, governance, and oversight at the regulatory and operational level.
Brisk Holloway is strongly internationally focused.
The website required should be simple, corporate, serious, and communicate professionalism, reliability and honesty. We are trying to give the company a feeling of being well established.
The attached files include the company logo, along with examples of company web page styles that we like.
The Brisk Holloway website need only be around five pages long (landing page, who we are, our services, our clients, contact), though don't feel limited to only five pages.
The existing website (www.briskholloway.example) was rushed and put together using Wix. We don't love the existing website as it looks too amateur, so don't use it as a template.
There is no requirement for any online sales tools to be included in the site. The site is purely informational, with the option of people making contact via email.

```html
<!DOCTYPE html>
<html lang="en">
<head>
<meta charset="utf-8">
<title>Brisk Holloway — Aviation Security Consulting</title>
<link rel="stylesheet" href="https://fonts.googleapis.com/css2?family=Open+Sans:wght@400;600;700&display=swap">
<style>
:root{
  --navy:#1f2b5e;
  --navy-dark:#18224b;
  --ink:#333;
  --muted:#666;
  --grey-band:#ebebeb;
  --card:#e6e6e6;
  --footer:#262626;
  --footer-line:#3a3a3a;
  --white:#fff;
}
*{box-sizing:border-box;margin:0;padding:0}
html,body{width:1200px;height:2565px;overflow:hidden}
body{font-family:"Open Sans",Arial,sans-serif;color:var(--ink);background:var(--white);position:relative}
.abs{position:absolute}

/* header */
.site-header{position:absolute;top:0;left:0;width:1200px;height:91px;background:var(--white)}
.brand{left:128px;top:20px;display:flex;align-items:center;gap:8px}
.brand-mark{width:30px;height:30px;background:var(--navy)}
.brand-name{font-size:22px;font-weight:700;color:var(--navy);line-height:1}
.brand-tag{font-size:9px;color:var(--navy);letter-spacing:.5px;margin-top:2px}
.main-nav{left:440px;top:38px;display:flex;gap:38px;font-size:13px;color:#444}
.main-nav a{color:inherit;text-decoration:none;padding-bottom:6px}
.main-nav a.active{border-bottom:2px solid var(--navy)}
.lang{left:955px;top:30px;width:115px}
.lang-toggle{background:#555;color:#fff;font-size:12px;padding:5px 10px;border-radius:3px;display:flex;justify-content:space-between}
.lang-menu{background:var(--navy);margin-top:2px;width:100px;font-size:10px;color:#fff;padding:3px 0}
.lang-menu li{list-style:none;padding:3px 6px}
.lang-menu li.current{background:#fff;color:var(--navy)}

/* hero */
.hero{position:absolute;top:91px;left:0;width:1200px;height:513px;background:linear-gradient(110deg,#2b3560 0%,#45507a 45%,#5a6488 70%,#3b4670 100%)}
.hero-arrow{position:absolute;top:222px;width:36px;height:70px;background:#fff;display:flex;align-items:center;justify-content:center}
.hero-arrow.prev{left:0}
.hero-arrow.next{right:0}

/* features */
.features{position:absolute;top:655px;left:128px;width:946px;display:flex;justify-content:space-between}
.feature{width:300px;display:flex;gap:14px}
.feature-icon{flex:none;width:44px;height:44px;border-radius:50%;background:var(--navy);display:flex;align-items:center;justify-content:center}
.feature h3{font-size:10px;font-weight:700;color:var(--navy);margin-bottom:4px}
.feature p{font-size:11px;line-height:1.55;color:var(--muted)}

/* who we are */
.who{position:absolute;top:798px;left:0;width:1200px;height:400px;background:var(--grey-band)}
.section-title{position:absolute;left:0;width:1200px;text-align:center;font-size:13px;font-weight:700;color:var(--navy)}
.section-title span{display:inline-block;padding:0 12px 6px;border-bottom:2px solid var(--navy)}
.who-photo{left:128px;top:108px;width:413px;height:268px;background:linear-gradient(90deg,#3a3e48 0%,#6e6f74 50%,#b9bcc2 100%)}
.who-copy{left:584px;top:98px;width:485px;font-size:13px;line-height:1.6;color:#333}
.who-list{left:584px;top:211px;width:485px}
.who-list li{list-style:none;background:var(--navy);color:#fff;font-size:12px;height:34px;display:flex;align-items:center;padding-left:12px;margin-bottom:30px;border-radius:2px}
.who-list li::before{content:"+";font-weight:700;margin-right:14px}

/* testimonials */
.testimonials-title{top:1222px}
.testimonials{position:absolute;top:1310px;left:128px;width:946px;display:flex;justify-content:space-between}
.testimonial{width:290px;height:206px;background:var(--card);position:relative;padding:50px 18px 0}
.quote-mark{position:absolute;left:14px;top:-10px;width:38px;height:38px;background:var(--navy);color:#fff;font-size:30px;font-weight:700;text-align:center;line-height:46px}
.avatar{position:absolute;left:54px;top:-10px;width:38px;height:38px;background:linear-gradient(#2e3a6b,#8a8fa8)}
.testimonial p{font-size:11px;line-height:1.6;color:#444}

/* banner */
.banner{position:absolute;top:1562px;left:0;width:1200px;height:342px;background:linear-gradient(90deg,#6d7180,#9a9da8 60%,#c3c5cc)}
.banner svg{position:absolute;left:0;top:0}
.banner-text{position:absolute;top:118px;left:0;width:1200px;text-align:center;color:#fff;font-size:24px;line-height:1.4}

/* clients */
.clients{position:absolute;top:1990px;left:40px;width:1120px;display:flex;justify-content:space-between;align-items:center}
.client{font-size:26px;font-weight:600;color:#333}

/* contact */
.footer{position:absolute;top:2212px;left:0;width:1200px;height:353px;background:var(--footer)}
.contact-band{position:absolute;top:2104px;left:128px;width:946px;height:148px;background:var(--navy)}
.field{position:absolute;background:#c9cbd3;color:#555;font-size:11px;padding:6px 10px;border-radius:2px}
.send{position:absolute;left:830px;top:40px;width:70px;height:30px;background:#fff;color:var(--navy);font-size:13px;display:flex;align-items:center;justify-content:center;border-radius:2px}
.contact-info{position:absolute;top:2262px;left:245px;display:flex;gap:60px;color:#fff;font-size:12px;align-items:flex-start}
.info-item{display:flex;gap:18px;align-items:center}
.info-lines{line-height:2.4}
.social{position:absolute;top:2370px;left:0;width:1200px;display:flex;justify-content:center;gap:28px}
.social span{width:40px;height:40px;border-radius:50%;background:#444}
.footer-nav{position:absolute;top:2457px;left:0;width:1200px;display:flex;justify-content:center;gap:50px;color:#fff;font-size:13px;font-weight:600}
.footer-legal{position:absolute;top:2535px;left:0;width:1200px;text-align:center;color:#bbb;font-size:10px;border-top:1px solid var(--footer-line);padding-top:6px}
</style>
</head>
<body>

<header class="site-header">
  <div class="abs brand">
    <div class="brand-mark"></div>
    <div>
      <div class="brand-name">Brisk Holloway</div>
      <div class="brand-tag">aviation security consulting</div>
    </div>
  </div>
  <nav class="abs main-nav">
    <a class="active">HOME</a><a>WHO WE ARE</a><a>OUR SERVICES</a><a>OUR CIENTS</a><a>CONTACT US</a>
  </nav>
  <div class="abs lang">
    <div class="lang-toggle"><span>Language</span><span>▾</span></div>
    <ul class="lang-menu">
      <li>Hindi</li><li class="current">English</li><li>German</li><li>France</li>
    </ul>
  </div>
</header>

<section class="hero" role="img" aria-label="Airport security officer screening a traveller's bag, blue-tinted photograph">
  <div class="hero-arrow prev"><svg width="14" height="26"><path d="M11 2 L3 13 L11 24" fill="none" stroke="#222" stroke-width="3"/></svg></div>
  <div class="hero-arrow next"><svg width="14" height="26"><path d="M3 2 L11 13 L3 24" fill="none" stroke="#222" stroke-width="3"/></svg></div>
</section>

<section class="features">
  <div class="feature">
    <div class="feature-icon"><svg width="22" height="22"><circle cx="11" cy="11" r="8" fill="none" stroke="#fff" stroke-width="2"/><path d="M5 11h12" stroke="#fff" stroke-width="2"/></svg></div>
    <div><h3>REGULATORS</h3><p>Strategic guidance, development of regulative, training, mentoring, and developing aviation security compliance tools.</p></div>
  </div>
  <div class="feature">
    <div class="feature-icon"><svg width="22" height="22"><path d="M3 17h16M6 14V8M11 14V5M16 14V10" stroke="#fff" stroke-width="2.5"/></svg></div>
    <div><h3>CAPACITY DEVELOPMENT</h3><p>Implementing economically sustainable solutions to aviation security challenges in the local environment.</p></div>
  </div>
  <div class="feature">
    <div class="feature-icon"><svg width="22" height="22"><path d="M2 12l8-1 5-8h2l-3 8 6 0 2-3h1l-1 4 1 4h-1l-2-3-6 0 3 8h-2l-5-8-8-1z" fill="#fff"/></svg></div>
    <div><h3>REGULATORS</h3><p>Ensuring security is incorporated into airport design, conducting security assessments and undertaking strategic planning.</p></div>
  </div>
</section>

<section class="who">
  <h2 class="section-title" style="top:26px"><span>WHO WE ARE</span></h2>
  <div class="abs who-photo" role="img" aria-label="Consultant inspecting a louvred security panel"></div>
  <p class="abs who-copy">Lorem Ipsum is simply dummy text of the printing and typesetting industry. Lorem Ipsum has been the industry's standard dummy text ever since the 1500s. orem Ipsum is simply dummy text of the printing and typesetting industry. Lorem Ipsum has been the industry's standard dummy text ever since the 1500s.</p>
  <ul class="abs who-list">
    <li>Lorem Ipsum is simply dummy text of the printing and typesetting</li>
    <li>Lorem Ipsum is simply dummy text of the printing and typesetting</li>
    <li>Lorem Ipsum is simply dummy text of the printing and typesetting</li>
  </ul>
</section>

<h2 class="section-title testimonials-title"><span>WHAT &nbsp;PEOPLE SAY !</span></h2>
<section class="testimonials">
  <article class="testimonial"><div class="quote-mark">“</div><div class="avatar" role="img" aria-label="Client portrait"></div><p>Lorem Ipsum is simply dummy text of the printing and typesetting industry. Lorem Ipsum has been the industry's standard dummy text ever since the 1500s, when an unknown printer took a galley of type and scrambled it to make a type specimen book. It has survived not only five centuries.</p></article>
  <article class="testimonial"><div class="quote-mark">“</div><div class="avatar" role="img" aria-label="Client portrait"></div><p>Lorem Ipsum is simply dummy text of the printing and typesetting industry. Lorem Ipsum has been the industry's standard dummy text ever since the 1500s, when an unknown printer took a galley of type and scrambled it to make a type specimen book. It has survived not only five centuries.</p></article>
  <article class="testimonial"><div class="quote-mark">“</div><div class="avatar" role="img" aria-label="Client portrait"></div><p>Lorem Ipsum is simply dummy text of the printing and typesetting industry. Lorem Ipsum has been the industry's standard dummy text ever since the 1500s, when an unknown printer took a galley of type and scrambled it to make a type specimen book. It has survived not only five centuries.</p></article>
</section>

<section class="banner" role="img" aria-label="Airport terminal interior with travellers at a check-in desk">
  <svg width="1200" height="342"><polygon points="0,0 640,0 1000,342 0,342" fill="#2e3a72" fill-opacity=".85"/></svg>
  <p class="banner-text">Brisk Holloway works with government and industry on aviation security<br>regulatory and operational strategy, governance, and oversight.</p>
</section>

<section class="clients">
  <span class="client">Meridale</span>
  <span class="client">Quillnet</span>
  <span class="client">Sunvale Financial</span>
  <span class="client">tickwell</span>
  <span class="client">The Nexus</span>
  <span class="client">Yodlo!</span>
</section>

<footer class="footer"></footer>

<section class="contact-band">
  <svg class="abs" style="left:90px;top:45px" width="50" height="55"><circle cx="20" cy="14" r="12" fill="#fff"/><path d="M0 52c0-18 10-26 20-26s20 8 20 26z" fill="#fff"/><circle cx="40" cy="38" r="9" fill="#fff" stroke="var(--navy)" stroke-width="2"/><path d="M36 38h8M40 34v8" stroke="var(--navy)" stroke-width="2"/></svg>
  <div class="field" style="left:180px;top:43px;width:140px">Name</div>
  <div class="field" style="left:350px;top:43px;width:140px">Email</div>
  <div class="field" style="left:525px;top:25px;width:260px;height:70px">Message</div>
  <div class="send">Send</div>
</section>

<section class="contact-info">
  <div class="info-item">
    <svg width="26" height="26"><path d="M2 6l7-3 8 3 7-3v17l-7 3-8-3-7 3z" fill="#fff"/></svg>
    <div class="info-lines">Viet , Streetxxxx<br>(xxx) idec xxxxx</div>
  </div>
  <div class="info-item" style="margin-top:12px">
    <svg width="20" height="22"><path d="M4 1h5l2 6-3 2c1 3 3 5 6 6l2-3 6 2v5c0 1-1 2-2 2C10 21 0 11 1 3c0-1 1-2 2-2z" fill="#fff"/></svg>
    <div>-1046-555465 &nbsp;&nbsp;&nbsp; -555-5550144</div>
  </div>
  <div class="info-item" style="margin-top:12px">
    <svg width="22" height="16"><rect x="1" y="1" width="20" height="14" fill="#fff"/><path d="M1 1l10 8 10-8" fill="none" stroke="#262626" stroke-width="1.5"/></svg>
    <div>info@briskholloway.example</div>
  </div>
</section>

<div class="social"><span></span><span></span><span></span><span></span></div>

<nav class="footer-nav"><span>HOME</span><span>WHO WE ARE</span><span>OUR SERVICES</span><span>OUR &nbsp;CIENTS</span><span>CONTACT US</span></nav>

<p class="footer-legal">Site Map &nbsp;| &nbsp;Privacy &nbsp;| &nbsp;Trem Use &nbsp;| &nbsp;©brisk holloway All right reserved.</p>

</body>
</html>
```